I am looking for label for our Candle Company

We need a label design for our new Candle Company based in Kansas City called Brisa Lumel Candle Company. (Pronounced "Fla-May"). We want to make sure we get the tick above the "e" in Brisa as Brisa is french for flame. We need a logo that we can use on the candles. We need it to include our name but we need to be able to edit the individual candle scent.

We are looking for a very elegant and vintage/old french look. We do not really want a lot (if any) bright color to the logo/design. I have enclosed our current log (of which we don't really like but are temporarily using) and a design that we love and would like to incorporate. You can see on our current label how we have to be able to include the individual candle scent name. I need to be able to edit this name.
Updates

Ilse, We have a couple of different label applications that we need to use the design on. We have a small label, a large label and a round label. I will work on getting you the dimensions tomorrow. Do you think there is any way to make a logo out of the middle part of this label? Doug

Target Market(s)

Anyone who loves candles.

Industry/Entity Type

It Company

Logo Text

Brisa Lumel Candle Company

Font styles to use
Decorative
Script

Requirements
Must have
• The ability to edit the candle scent name so that we can use it on every different candle that we make.
Should not have
• Too many vibrant colors.

```html
<!DOCTYPE html>
<html lang="en">
<head>
<meta charset="utf-8">
<title>Brisa Lumel Candle Company – Scent Label</title>
<link rel="stylesheet" href="https://fonts.googleapis.com/css2?family=Pinyon+Script&family=Poiret+One&display=swap">
<style>
  :root {
    --page: #ffffff;
    --label-blush: #e6d8d2;
    --pattern-blush: #dccbc4;
    --cartouche-cream: #efe5e1;
    --ornament-brown: #4a3033;
    --band-brown: #3a2326;
    --band-text: #eadfda;
    --ink-brown: #3a2326;
    --swirl-tone: #cdb9b2;
  }
  * { margin: 0; padding: 0; box-sizing: border-box; }
  html, body {
    width: 1200px;
    height: 1200px;
    overflow: hidden;
    background: var(--page);
  }
  .canvas {
    position: relative;
    width: 1200px;
    height: 1200px;
  }
  .label {
    position: absolute;
    left: 177px;
    top: 270px;
    width: 846px;
    height: 625px;
    background: var(--label-blush);
    overflow: hidden;
  }
  .damask-field {
    position: absolute;
    inset: 0 0 97px 0;
    background: radial-gradient(ellipse at center, var(--label-blush) 35%, var(--pattern-blush) 100%);
  }
  .cartouche {
    position: absolute;
    left: 170px;
    top: 54px;
    width: 506px;
    height: 416px;
  }
  .brand {
    position: absolute;
    left: 0;
    right: 0;
    top: 196px;
    text-align: center;
    color: var(--ink-brown);
  }
  .brand-name {
    display: block;
    font-family: "Pinyon Script", cursive;
    font-weight: 400;
    font-size: 76px;
    line-height: 1;
    letter-spacing: 0;
  }
  .brand-sub {
    display: block;
    margin-top: 4px;
    font-family: "Poiret One", sans-serif;
    font-size: 25px;
    letter-spacing: 2px;
  }
  .scent-band {
    position: absolute;
    left: 0;
    right: 0;
    bottom: 0;
    height: 97px;
    background: var(--band-brown);
    display: flex;
    align-items: center;
    justify-content: center;
    gap: 60px;
  }
  .scent-name {
    font-family: "Poiret One", sans-serif;
    color: var(--band-text);
    font-size: 46px;
    letter-spacing: 2px;
    line-height: 1;
    padding-top: 4px;
  }
  .band-swirl {
    width: 34px;
    height: 22px;
    border-radius: 50%;
    background: var(--swirl-tone);
  }
</style>
</head>
<body>
  <main class="canvas">
    <section class="label">
      <div class="damask-field" role="img" aria-label="Faint blush damask wallpaper pattern"></div>

      <svg class="cartouche" viewBox="0 0 506 416" role="img" aria-label="Ornate baroque scroll frame with small flourishes above and below the name">
        <ellipse cx="253" cy="208" rx="236" ry="190" fill="var(--cartouche-cream)"/>
        <ellipse cx="253" cy="208" rx="236" ry="190" fill="none" stroke="var(--ornament-brown)" stroke-width="26" opacity="0.85"/>
        <ellipse cx="253" cy="102" rx="44" ry="11" fill="var(--ornament-brown)" opacity="0.8"/>
        <ellipse cx="253" cy="318" rx="44" ry="11" fill="var(--ornament-brown)" opacity="0.8"/>
      </svg>

      <div class="brand">
        <span class="brand-name">Brisa Lumel</span>
        <span class="brand-sub">CANDLE COMPANY</span>
      </div>

      <div class="scent-band">
        <span class="band-swirl" role="img" aria-label="Small scroll flourish"></span>
        <span class="scent-name">GIRLS NIGHT OUT</span>
        <span class="band-swirl" role="img" aria-label="Small scroll flourish"></span>
      </div>
    </section>
  </main>
</body>
</html>
```